Belzo business card

I'm a hack at Illustrator, but have put together a set of business cards as attached. If someone could please improve these including good font selection, standard font sizes and spacing, nice layout and symmetry. Rear side the same on all cards. Basically make these cards into something impressive and professional.
Updates

Official logo just uploaded, please use these colours

Target Market(s)

50+ year old married couples

Industry/Entity Type

Business

Requirements
Must have
• Professional
Should not have
• Silly, cartoony

```html
<!DOCTYPE html>
<html lang="en">
<head>
<meta charset="utf-8">
<title>Belzo business card</title>
<link href="https://fonts.googleapis.com/css2?family=Lato:wght@400;700&display=swap" rel="stylesheet">
<style>
  :root {
    --page: #e9e6e2;
    --card-white: #ffffff;
    --card-black: #111113;
    --brand-blue: #25328f;
    --brand-blue-light: #4a5bd0;
    --ink-light: #e6e6e6;
    --shadow: rgba(0, 0, 0, 0.18);
  }
  * { box-sizing: border-box; margin: 0; padding: 0; }
  html, body {
    width: 1200px;
    height: 900px;
    overflow: hidden;
    background: var(--page);
    font-family: "Lato", sans-serif;
  }
  .sheet {
    width: 1200px;
    height: 900px;
    display: flex;
    flex-direction: column;
    align-items: center;
    justify-content: center;
    gap: 60px;
  }
  .card {
    position: relative;
    width: 620px;
    height: 354px;
    border-radius: 22px;
    overflow: hidden;
    box-shadow: 0 10px 28px var(--shadow);
  }
  .card--back { background: var(--card-white); }
  .card--front { background: var(--card-black); }

  .brand {
    display: flex;
    align-items: center;
    gap: 14px;
  }
  .brand__mark {
    width: 18px;
    height: 18px;
    background: var(--brand-blue);
  }
  .brand__name {
    font-weight: 700;
    color: var(--brand-blue);
    letter-spacing: 0.32em;
    line-height: 1;
  }

  .card--back .brand {
    position: absolute;
    inset: 0;
    justify-content: center;
  }
  .card--back .brand__name { font-size: 56px; }

  .card__panel {
    position: absolute;
    inset: 0;
    width: 100%;
    height: 100%;
  }
  .card__panel .panel-white { fill: var(--card-white); }
  .card__panel .panel-arc { fill: var(--brand-blue); }

  .contact {
    position: absolute;
    left: 34px;
    top: 48px;
    color: var(--ink-light);
    font-size: 14px;
    line-height: 1.5;
    white-space: nowrap;
  }
  .contact__name {
    color: var(--brand-blue-light);
    font-weight: 700;
    font-size: 17px;
  }
  .contact__role { margin-bottom: 14px; }
  .contact__row dt {
    display: inline;
    color: var(--brand-blue-light);
    font-weight: 700;
  }
  .contact__row dd { display: inline; }

  .card--front .brand {
    position: absolute;
    left: 318px;
    right: 10px;
    top: 0;
    bottom: 0;
    justify-content: center;
  }
  .card--front .brand__name { font-size: 42px; }
</style>
</head>
<body>
<main class="sheet">
  <section class="card card--back" aria-label="Card back">
    <div class="brand">
      <span class="brand__mark"></span>
      <span class="brand__name">BELZO</span>
    </div>
  </section>

  <section class="card card--front" aria-label="Card front">
    <svg class="card__panel" viewBox="0 0 620 354" aria-hidden="true">
      <path class="panel-arc" d="M350,0 Q250,177 350,354 L362,354 Q262,177 362,0 Z"/>
      <path class="panel-white" d="M362,0 Q262,177 362,354 L620,354 L620,0 Z"/>
    </svg>
    <div class="contact">
      <p class="contact__name">Daniel Whitmore</p>
      <p class="contact__role">Product &amp; Projects Manager</p>
      <dl>
        <div class="contact__row"><dt>M :</dt> <dd>0491 570 156</dd></div>
        <div class="contact__row"><dt>Ph :</dt> <dd>(+61) 03 9012 4478</dd></div>
        <div class="contact__row"><dt>D :</dt> <dd>30 9012 4470</dd></div>
        <div class="contact__row"><dt>Mail :</dt> <dd>daniel.whitmore@belzo.com.au</dd></div>
        <div class="contact__row"><dt>Web :</dt> <dd>www.belzo.com.au</dd></div>
      </dl>
    </div>
    <div class="brand">
      <span class="brand__mark"></span>
      <span class="brand__name">BELZO</span>
    </div>
  </section>
</main>
</body>
</html>
```